Need 3 posters for in-store display

Hi Marlene,

Hope you are well.
I need 3 posters for display in my restaurant.

Poster 1: To be print in A1 size vertical
Title: SLURPALICIOUS DEAL $19.50
Choose any Pho OR Noodle Salads
Choose Spring Rolls (5 rolls) OR Ricepaper Rolls (2 rolls)
Choose any Cans OR Water

What I like to see:
- These poster will be place near my counter so I want it to grab customer attention.
- You must use photos to show products
- Make it easy to understand and for customer to follow

Poster 2: To be print in A4 size vertical
Title: ADD TO YOUR ORDER
SpringRolls (Crab / vegetarian) $6 / 5 rolls
Extra Meat $2
Extra Noodles $1
Extra Vegs $1.5
Extra Tofu $2
Extra Crackling $3

Poster 3: To be print in A1 size vertical
Title: BROTH BONANZA BASH
Catering Menu Options:
- PHO (Beef, Chicken, Vegan) $12.50 per bowl
- NOODLE SALADS (Beef, Chicken, BBQ Pork, Vegan) $12.50 per bowl
- SpringRolls (Crab / vegetarian) $12.50 for 10 rolls
- Ricepaper Rolls (Prawn, Beef, Chicken, BBQ Pork, Tofu) $12.5 / 5 rolls
- Fried Rice (Prawn, Tofu) $50 per tray (serve 5-6)

Terms & Conditions for All Catering Orders:
1) Minimum orders $200 (Pick-Up from shop Only)
2) All orders must be paid upfront
3) Requires $300 bond for Soup Tank
4) Please give us 48hours notice

Industry/Entity Type

Restaurant

Requirements
Nice to have
• For the SLURPALICIOUS DEAL
• it would be nice to have an image of the battle of water to visually complete the meal deal
• please see attachment of the Kestrel Ridge Water

```html
<!DOCTYPE html>
<html lang="en">
<head>
<meta charset="utf-8">
<title>Add To Your Order – A4 Poster</title>
<link rel="stylesheet" href="https://fonts.googleapis.com/css2?family=Lobster&family=Great+Vibes&family=Oswald:wght@500;600&family=Raleway:ital,wght@1,400&display=swap">
<style>
  :root {
    --stage: #d9d9d9;
    --header-top: #2e2e2e;
    --header-mid: #8a8a8a;
    --body-bg: #474747;
    --body-dark: #343434;
    --silver: #f2f2f2;
    --silver-shade: #bdbdbd;
    --white: #ffffff;
    --price-orange: #f39a62;
    --badge-bg: #ececec;
    --badge-ink: #5a1a16;
    --photo-light: #cfa16a;
    --photo-dark: #8f8f8f;
  }
  * { margin: 0; padding: 0; box-sizing: border-box; }
  html, body { width: 1200px; height: 900px; overflow: hidden; background: var(--stage); }

  .poster {
    position: absolute; left: 294px; top: 20px;
    width: 611px; height: 860px; overflow: hidden;
    background: radial-gradient(ellipse at 50% 60%, var(--body-bg) 0%, var(--body-dark) 100%);
    box-shadow: 0 6px 18px rgba(0,0,0,.35);
  }
  .poster-header {
    position: absolute; left: 0; top: 0; width: 100%; height: 244px;
    background: radial-gradient(ellipse at 50% 85%, var(--header-mid) 0%, #5a5a5a 40%, var(--header-top) 100%);
  }
  .header-band {
    position: absolute; left: 0; top: 238px; width: 100%; height: 12px;
    background: linear-gradient(180deg, #9a9a9a 0%, #f4f4f4 40%, #6a6a6a 100%);
  }
  .title {
    position: absolute; left: 0; top: 6px; width: 100%;
    font-family: 'Lobster', cursive; font-weight: 400; font-size: 86px; line-height: 72px;
    text-align: center; color: var(--silver);
    text-shadow: 0 3px 0 var(--silver-shade), 0 5px 8px rgba(0,0,0,.5);
  }
  .title .line-one { display: block; padding-left: 40px; }
  .title .line-two { display: block; padding-left: 10px; }
  .flourish {
    position: absolute; left: 140px; width: 351px; height: 56px;
    background: linear-gradient(180deg, rgba(255,255,255,.18), rgba(255,255,255,.06));
    border-radius: 28px;
  }
  .flourish--top { top: 180px; }
  .flourish--bottom { top: 787px; }

  .item-heading {
    position: absolute; left: 26px; top: 262px; white-space: nowrap;
    color: var(--white); font-family: 'Great Vibes', cursive; font-weight: 400;
  }
  .item-name { font-size: 64px; }
  .item-dash { font-family: 'Raleway', sans-serif; font-size: 34px; margin: 0 6px; }
  .item-variants { font-size: 40px; }

  .product-photo {
    position: absolute; left: 0; top: 345px; width: 405px; height: 305px;
    background: radial-gradient(ellipse at 42% 45%, var(--photo-light) 0%, #b7a58f 45%, var(--photo-dark) 100%);
  }

  .price-badge {
    position: absolute; left: 418px; top: 343px; width: 176px; height: 176px;
    border-radius: 50%; background: var(--badge-bg);
    box-shadow: 0 2px 6px rgba(0,0,0,.4);
    text-align: center; color: var(--badge-ink);
    font-family: 'Oswald', sans-serif;
  }
  .price-badge::before {
    content: ""; position: absolute; inset: 9px;
    border: 1.5px dashed #777; border-radius: 50%;
  }
  .price-amount { display: block; margin-top: 24px; font-size: 66px; font-weight: 600; line-height: 72px; }
  .price-qty { display: block; font-size: 33px; font-weight: 500; line-height: 38px; }

  .extras {
    position: absolute; left: 0; width: 100%; text-align: center;
    font-family: 'Raleway', sans-serif; font-style: italic; font-size: 21px;
    color: var(--white); white-space: nowrap;
  }
  .extras--one { top: 648px; padding-left: 12px; }
  .extras--two { top: 708px; }
  .extras .price { font-family: 'Oswald', sans-serif; font-style: normal; font-weight: 500; font-size: 30px; color: var(--price-orange); margin-left: 4px; }
  .extras .sep { margin: 0 8px; font-style: normal; }
  .rule { position: absolute; height: 0; border-top: 2px dashed var(--white); }
  .rule--one { left: 126px; width: 364px; top: 695px; }
  .rule--two { left: 34px; width: 544px; top: 757px; }
</style>
</head>
<body>
  <main class="poster">
    <header class="poster-header">
      <h1 class="title"><span class="line-one">Add To</span><span class="line-two">Your Order</span></h1>
      <div class="flourish flourish--top" role="img" aria-label="Decorative scroll flourish"></div>
    </header>
    <div class="header-band"></div>

    <h2 class="item-heading"><span class="item-name">Spring Rolls</span><span class="item-dash">–</span><span class="item-variants">Crab / Vegetarian</span></h2>

    <div class="product-photo" role="img" aria-label="Photo of golden fried spring rolls on a white plate"></div>

    <div class="price-badge">
      <span class="price-amount">$6</span>
      <span class="price-qty">5 ROLLS</span>
    </div>

    <p class="extras extras--one">Extra Meat<span class="price">$2</span><span class="sep">–</span>Extra Noodles<span class="price">$1</span></p>
    <div class="rule rule--one"></div>
    <p class="extras extras--two">Extra Vegs<span class="price">$1.5</span><span class="sep">–</span>Extra Tofu<span class="price">$2</span><span class="sep">–</span>Extra Crackling<span class="price">$3</span></p>
    <div class="rule rule--two"></div>

    <div class="flourish flourish--bottom" role="img" aria-label="Decorative scroll flourish"></div>
  </main>
</body>
</html>
```